Slim Can Designs! Single Origin Coffee Cold Brew Coffee Cans

Amber Heron is a lifestyle brand with a focus on producing coffee. We need a three labels designed for our Cold Brew Cans. These will be 12 oz. slim cans for cold brew coffee. Each can will represent a different flavor profile tied to a virtue. Template Attached. We only have three products for cold brew cans. Please also review all the files included in our project for reference.
1. Gratitude : Toffee, Smokey, Chocolate
Things to include: Single Origin Coffee Dark Roast / Bold and Strong
2. Patience : Caramel, Chocolate, Dried Mango / Bright and Sparkling
Things to include: Single Origin Coffee Medium Roast
3. Kindness : Berry, Citrus, Floral / Smooth and Rich
Things to include: Single Origin Coffee Light Roast
All cans should include:
1. our logo. and brand colors.
2. all virtue icons if possible ?
3. Nutrition Label attached. Use this for all three, it may change but please use for placeholder.
4. Barcode
5. Net wt. 12oz
6. Ingredients : Single Origin Coffee, Water
7. BE KIND DRINK COFFEE
8. EST 2007
9. Roasted in Portland
10. Our business name and address:
Amber Heron Coffee Roasters
Portland, Oregon
web amberheronco.com
instagram amberheronco
11. Ethically Sourced Coffee Icon: if you can create one
12. Please recycle icon
13. Shake Lightly and Serve Chilled
14. Caffeine Content 200mg. : this might change between product but please use this as a placeholder for now.
15.

These designs should be cohesive and have some connection to our other brand element to tie together with our other current product designs. We are looking for sleek but fun and bold with colors and elements.

Target Market(s)

Mass market

Industry/Entity Type

Coffee

Font styles to use
Sans Serif
Other font styles liked:
• Please refer to our brand kit

Requirements
Must have
• Please refer to description
Nice to have

```html
<!DOCTYPE html>
<html lang="en">
<head>
<meta charset="utf-8">
<title>Amber Heron – Gratitude Cold Brew Can Label</title>
<link rel="stylesheet" href="https://fonts.googleapis.com/css2?family=Oswald:wght@500;600&family=Montserrat:wght@300;400&family=Roboto:wght@400;700;900&display=swap">
<style>
  :root{
    --peach:#f9d3a3;
    --teal:#4f9089;
    --teal-light:#d6ebe8;
    --navy:#2e3a5c;
    --rose:#c4546c;
    --cream:#f2e6d8;
    --white:#ffffff;
  }
  *{box-sizing:border-box;margin:0;padding:0}
  html,body{width:1199px;height:1200px;overflow:hidden;background:var(--peach)}
  .canvas{position:relative;width:1199px;height:1200px}
  .label{position:absolute;left:50px;top:455px;width:1100px;height:289px;background:var(--teal);overflow:hidden}
  .panel{position:absolute;top:0;height:289px}
  .pattern-band{position:absolute;left:0;bottom:0;width:100%;height:37px;
    background:linear-gradient(90deg,var(--navy),var(--rose) 18%,var(--navy) 36%,var(--teal) 52%,var(--navy) 68%,var(--rose) 84%,var(--navy))}

  /* nutrition panel */
  .nutrition{left:0;width:316px}
  .facts{position:absolute;left:23px;top:12px;width:99px;background:var(--white);color:#000;
    font-family:"Roboto",sans-serif;font-size:4.6px;line-height:1.35;padding:3px 4px;border:1px solid #000}
  .facts h3{font-weight:900;font-size:10px;line-height:1;border-bottom:1px solid #000;padding-bottom:1px}
  .facts .big{font-weight:900;font-size:8px;display:flex;justify-content:space-between;border-top:3px solid #000;border-bottom:2px solid #000;margin:1px 0}
  .facts .row{display:flex;justify-content:space-between;border-bottom:.5px solid #000}
  .facts .row.indent span:first-child{padding-left:5px}
  .facts .thick{border-bottom:3px solid #000}
  .facts .note{font-size:3.8px;margin-top:2px}
  .recycle{position:absolute;left:148px;top:18px;width:32px;height:32px}
  .address{position:absolute;left:190px;top:14px;height:190px;writing-mode:vertical-rl;transform:rotate(180deg);
    font-family:"Oswald",sans-serif;font-weight:500;font-size:9px;line-height:1.2;color:var(--white);text-transform:uppercase;text-align:right}

  /* brand panel */
  .brand{left:316px;width:148px}
  .contact-frame{position:absolute;left:0;top:36px;width:28px;height:170px;border:1.5px solid var(--teal-light);border-left:none;border-radius:0 12px 12px 0;
    display:flex;justify-content:center;align-items:center}
  .contact{writing-mode:vertical-rl;transform:rotate(180deg);font-family:"Montserrat",sans-serif;font-size:6px;color:var(--white);line-height:1.5;text-transform:uppercase;white-space:nowrap}
  .contact .sep{display:inline-block;width:.8px;height:10px;background:var(--white);margin:0 4px;vertical-align:middle}
  .contact .lower{text-transform:none}
  .brand-name{position:absolute;left:58px;top:12px;height:220px;writing-mode:vertical-rl;transform:rotate(180deg);
    font-family:"Montserrat",sans-serif;font-weight:300;font-size:25px;line-height:1.05;color:var(--teal-light);letter-spacing:1px;text-transform:uppercase;text-align:right}

  /* front panel */
  .front{left:464px;width:166px}
  .front-art{position:absolute;left:0;top:0;width:166px;height:170px;
    background:linear-gradient(160deg,var(--navy) 0%,var(--cream) 30%,var(--navy) 48%,var(--rose) 62%,var(--navy) 80%)}
  .banner{position:absolute;left:0;top:104px;width:166px;height:82px;background:var(--navy);border-radius:0 0 16px 16px;text-align:center}
  .virtue{font-family:"Oswald",sans-serif;font-weight:600;font-size:31px;color:var(--cream);letter-spacing:.5px;line-height:1;margin-top:16px}
  .notes{font-family:"Oswald",sans-serif;font-weight:500;font-size:8.5px;color:var(--white);margin-top:7px}
  .front-brand{position:absolute;left:0;top:60px;width:100%;text-align:center;font-family:"Oswald",sans-serif;font-weight:500;font-size:10px;color:var(--cream);letter-spacing:1px;text-transform:uppercase}
  .icons{position:absolute;left:16px;top:203px;width:134px;display:flex;justify-content:space-between}
  .icons span{width:14px;height:14px;border-radius:50%;background:var(--cream)}
  .net{position:absolute;left:0;top:226px;width:100%;text-align:center;font-family:"Oswald",sans-serif;font-weight:500;font-size:7px;line-height:1.15;color:var(--white);text-transform:uppercase}

  /* single origin strip */
  .origin{left:630px;width:98px;display:flex;justify-content:center;align-items:flex-start}
  .origin p{margin-top:12px;writing-mode:vertical-rl;transform:rotate(180deg);font-family:"Montserrat",sans-serif;font-weight:300;font-size:11px;letter-spacing:4px;color:var(--teal-light);text-transform:uppercase}

  /* info panel */
  .info{left:728px;width:372px}
  .info-brand{position:absolute;left:0;top:18px;width:100%;text-align:center;font-family:"Oswald",sans-serif;font-weight:500;font-size:10px;letter-spacing:1px;color:var(--navy);text-transform:uppercase}
  .claim{position:absolute;font-family:"Oswald",sans-serif;font-weight:500;color:var(--white);text-transform:uppercase;text-shadow:2px 2px 0 var(--navy);white-space:nowrap;line-height:1}
  .ingredients{left:36px;top:71px;font-size:28px}
  .kind{left:78px;top:116px;font-size:28px}
  .cup{position:absolute;left:38px;top:114px;width:36px;height:42px}
  .roast-box{position:absolute;left:30px;top:156px;width:330px;height:90px}
  .roast{left:54px;top:170px;font-size:20px}
  .bold{left:54px;top:205px;font-size:19px}
</style>
</head>
<body>
<main class="canvas">
  <section class="label" aria-label="Gratitude cold brew can label, flat">

    <div class="panel nutrition">
      <div class="facts">
        <h3>Nutrition Facts</h3>
        <div>1 servings per container</div>
        <div class="row thick"><b>Serving size</b><b>1 can (354mL)</b></div>
        <div style="font-weight:700">Amount per serving</div>
        <div class="big"><span>Calories</span><span>20</span></div>
        <div class="row" style="justify-content:flex-end"><b>% Daily Value*</b></div>
        <div class="row"><span><b>Total Fat</b> 0g</span><span>0%</span></div>
        <div class="row indent"><span>Saturated Fat 0g</span><span>0%</span></div>
        <div class="row indent"><span>Trans Fat 0g</span><span></span></div>
        <div class="row"><span><b>Cholesterol</b> 0mg</span><span>0%</span></div>
        <div class="row"><span><b>Sodium</b> 8mg</span><span>0%</span></div>
        <div class="row"><span><b>Total Carbohydrate</b> 3g</span><span>1%</span></div>
        <div class="row indent"><span>Dietary Fiber 0g</span><span>0%</span></div>
        <div class="row indent"><span>Total Sugars 0g</span><span></span></div>
        <div class="row indent"><span>Includes 0g Added Sugars</span><span>0%</span></div>
        <div class="row thick"><span><b>Protein</b> 1g</span><span></span></div>
        <div class="row"><span>Vitamin D 0mcg</span><span>0%</span></div>
        <div class="row"><span>Calcium 20mg</span><span>2%</span></div>
        <div class="row"><span>Iron 0mg</span><span>0%</span></div>
        <div class="row thick"><span>Potassium 510mg</span><span>10%</span></div>
        <p class="note">*Percent Daily Values are based on a 2,000 calorie diet.</p>
      </div>
      <svg class="recycle" viewBox="0 0 32 32" aria-label="Please recycle">
        <g fill="none" stroke="var(--white)" stroke-width="3" stroke-linecap="round" stroke-linejoin="round">
          <path d="M12 6 L16 3 L20 9"/><path d="M20 9 l-4 0"/><path d="M20 9 l1-4"/>
          <path d="M26 14 L29 22 L23 26"/><path d="M23 26 l1-4"/><path d="M23 26 l-4-1"/>
          <path d="M10 27 L3 22 L6 15"/><path d="M6 15 l2 3"/><path d="M6 15 l-3 2"/>
        </g>
      </svg>
      <p class="address">Our business name and address:<br>Amber Heron Coffee Roasters<br>Portland, Oregon</p>
    </div>

    <div class="panel brand">
      <div class="contact-frame">
        <p class="contact"><span class="lower">@amberheronco</span><br><span class="lower">amberheronco.com</span></p>
      </div>
      <div class="contact-frame" style="left:44px;top:36px;border:none;width:auto"></div>
      <p class="brand-name">Amber Heron<br>Coffee Roasters</p>
      <p class="contact" style="position:absolute;left:34px;top:60px">Est 2007<span class="sep"></span>Roasted in Portland</p>
    </div>

    <div class="panel front">
      <div class="front-art" role="img" aria-label="Decorative swirl pattern in navy, cream and rose"></div>
      <p class="front-brand">Amber Heron</p>
      <div class="banner">
        <h1 class="virtue">GRATITUDE</h1>
        <p class="notes">TOFFEE, SMOKEY, CHOCOLATE</p>
      </div>
      <div class="icons" aria-label="Virtue icons"><span></span><span></span><span></span><span></span><span></span><span></span><span></span></div>
      <p class="net">Net Wt. 12 oz<br>Caffeine Content 200mg</p>
    </div>

    <div class="panel origin"><p>Single Origin Coffee</p></div>

    <div class="panel info">
      <p class="info-brand">Amber Heron</p>
      <p class="claim ingredients">Single Origin Coffee, Water</p>
      <svg class="cup" viewBox="0 0 36 42" aria-hidden="true">
        <rect x="4" y="4" width="28" height="6" rx="2" fill="var(--white)" stroke="var(--navy)" stroke-width="1.5"/>
        <path d="M7 10 L29 10 L26 40 L10 40 Z" fill="var(--white)" stroke="var(--navy)" stroke-width="1.5"/>
        <circle cx="18" cy="24" r="6" fill="var(--teal)"/>
      </svg>
      <p class="claim kind">Be Kind Drink Coffee</p>
      <svg class="roast-box" viewBox="0 0 330 90" aria-hidden="true">
        <polygon points="8,6 318,0 326,44 300,84 4,90 12,50" fill="var(--navy)"/>
      </svg>
      <p class="claim roast">Single Origin Coffee Dark Roast</p>
      <p class="claim bold">Bold and Strong</p>
    </div>

    <div class="pattern-band" role="img" aria-label="Decorative swirl pattern band in navy, rose and teal"></div>
  </section>
</main>
</body>
</html>
```